ambitious event and festival agency from austria needs fresh business card design

A new design is due for the new headquarters and the new challenges. We organize events for different target groups from 16 to 60 years. The design should therefore be straightforward and not confused, so we are open to new colors and the logo may also be changed. In general, however, the most interesting suggestions are the most interesting ones. after this order we are looking for more graphics for quillvane facebook instagramm homepage etc A new design is due for the new headquarters and the new challenges. We organize events for different target groups from 16 to 60 years. The design should therefore be straightforward and not confused, so we are open to new colors and the logo may also be changed. In general, however, the most interesting suggestions are the most interesting ones. after this order we are looking for more graphics for quillvane facebook instagramm homepage etc A new design is due for the new headquarters and the new challenges. We organize events for different target groups from 16 to 60 years. The design should therefore be straightforward and not confused, so we are open to new colors and the logo may also be changed. In general, however, the most interesting suggestions are the most interesting ones. after this order we are looking for more graphics for quillvane facebook instagramm homepage etc
Updates

Reason: I am sorry for this decision but i need some more time. No new designs please, there are so many good ones and I will have made a decision in the next 3 days.

Target Market(s)

Industry/Entity Type

Business

Font styles to use
Serif
Sans Serif

Colors

Designer to choose colors to be used in the design.

Requirements
Must have
Nice to have
Should not have

```html
<!DOCTYPE html>
<html lang="de">
<head>
<meta charset="utf-8">
<title>quillvane – Visitenkarte</title>
<link rel="stylesheet" href="https://fonts.googleapis.com/css2?family=Roboto:wght@400;500;700&family=Roboto+Condensed:wght@400;700&display=swap">
<style>
  :root {
    --backdrop: #e4e4e4;
    --card-white: #f4f4f4;
    --brand-red: #b02533;
    --brand-grey: #626a6c;
    --text-grey: #5d6264;
    --divider: #b9bcbd;
  }
  * { margin: 0; padding: 0; box-sizing: border-box; }
  html, body {
    width: 1200px; height: 960px; overflow: hidden;
    background: var(--backdrop);
    font-family: "Roboto", Arial, sans-serif;
  }
  .canvas { position: relative; width: 1200px; height: 960px; }

  .card { position: absolute; width: 600px; height: 342px; }
  .card-front { left: 314px; top: 113px; background: var(--card-white); }
  .card-back { left: 311px; top: 472px; background: var(--brand-red); }

  .wordmark {
    position: absolute; left: 50px; top: 152px; width: 236px;
    display: flex; align-items: center; gap: 8px;
    font-family: "Roboto", Arial, sans-serif;
    font-weight: 500; font-size: 36px; line-height: 1;
    color: var(--brand-red); letter-spacing: -0.5px;
  }
  .wordmark-square { width: 12px; height: 12px; background: var(--brand-red); }

  .divider {
    position: absolute; left: 315px; top: 82px;
    width: 1px; height: 186px; background: var(--divider);
  }

  .contact { position: absolute; left: 346px; top: 84px; color: var(--text-grey); }
  .person-name {
    font-family: "Roboto Condensed", "Arial Narrow", sans-serif;
    font-weight: 700; font-size: 22px; color: var(--brand-red); line-height: 22px;
  }
  .person-role {
    font-family: "Roboto Condensed", "Arial Narrow", sans-serif;
    font-size: 16px; line-height: 22px; letter-spacing: 0.3px;
  }
  .address { margin-top: 10px; font-size: 14.5px; line-height: 18px; }
  .address .company { font-weight: 700; color: #4d5153; }
  .channels { margin-top: 10px; list-style: none; font-size: 14.5px; line-height: 19px; }
  .channels li { display: flex; align-items: center; gap: 8px; }
  .channels svg { width: 13px; height: 13px; fill: var(--brand-red); flex: none; }

  .edge-band { position: absolute; left: 0; bottom: 0; width: 600px; height: 14px; display: block; }

  .back-name {
    position: absolute; left: 0; right: 0; top: 140px; text-align: center;
    font-weight: 500; font-size: 44px; color: var(--card-white); letter-spacing: -0.5px;
  }
  .back-url {
    position: absolute; left: 0; right: 0; top: 289px; text-align: center;
    font-size: 14px; letter-spacing: 6.2px; color: var(--card-white);
  }
</style>
</head>
<body>
<main class="canvas">
  <section class="card card-front">
    <div class="wordmark"><span class="wordmark-square"></span><span>quillvane</span></div>
    <div class="divider"></div>
    <div class="contact">
      <h1 class="person-name">MARKUS FELDHOFER</h1>
      <p class="person-role">GESCHAFTSFUHRER</p>
      <p class="address"><span class="company">quillvane</span><br>Ahornweg 14<br>A4630 talbach</p>
      <ul class="channels">
        <li><svg viewBox="0 0 16 16" aria-hidden="true"><path d="M3.6 1.2l2.4 2.6-1.3 2a9 9 0 0 0 5.5 5.5l2-1.3 2.6 2.4-1.5 2.1C7.3 14.8 1.2 8.7 1.5 2.7z"/></svg>+43 650 418 273 0</li>
        <li><svg viewBox="0 0 16 16" aria-hidden="true"><path d="M1 3h14v1.4L8 9 1 4.4z M1 6l7 4.6L15 6v7H1z"/></svg>m.feldhofer@quillvane.eu</li>
        <li><svg viewBox="0 0 16 16" aria-hidden="true"><circle cx="8" cy="8" r="7"/><path d="M4 5h3l1 2-2 1 1 3-2 1zM10 3l2 2-1 2-2-1z" fill="#f4f4f4"/></svg>www.quillvane.eu</li>
      </ul>
    </div>
    <svg class="edge-band" viewBox="0 0 600 14" preserveAspectRatio="none" aria-hidden="true">
      <polygon points="0,0 393,0 389,14 0,14" fill="var(--brand-red)"/>
      <polygon points="397,0 600,0 600,14 393,14" fill="var(--brand-grey)"/>
    </svg>
  </section>

  <section class="card card-back">
    <p class="back-name">quillvane</p>
    <p class="back-url">www.quillvane.eu</p>
  </section>
</main>
</body>
</html>
```